Morevo - Augmented Reality Mobile application

We need a logo design for new mobile application. The overall objective of the application is to build a digital content delivery tool for scanning and recognizing of an image (marker) through a mobile application. The provision of digital content to the user takes place via augmeted reality and / or redirecting the user to a given digital content source.We don`t have any color scheme yet, but we have been thinking about something colorful. We are open for ideas.I have uploaded our working logos, but we are not strongly engaged with them.
Updates

Hello everybody, I have increased the budget of the project Regards

Target Market(s)

Entertainment; Education;

Industry/Entity Type

Entertainment

Logo Text

"Morevo" is the name of the product. We want a logo enough distinguishable to be recognized even without the text

Font styles to use
Serif
Sans Serif

Colors

Designer to choose colors to be used in the design.

Requirements
Must have
• We have attached a document with some information about the product. Feel free to use whatever found useful in it.
• We are not looking for the same design, rather an alternative one. We need all of the screens mentioned in the document
Nice to have
Should not have

```html
<!DOCTYPE html>
<html lang="en">
<head>
<meta charset="utf-8">
<title>Morevo – app screens</title>
<link rel="stylesheet" href="https://fonts.googleapis.com/css2?family=Montserrat:wght@400;500;600;700&family=Open+Sans:wght@400;600&display=swap">
<style>
:root{
  --page:#f8f7f5;
  --bar:#232a38;
  --orange:#ff6a0d;
  --blue:#2e5fd0;
  --ink:#2a2d33;
  --screen-mid:#fdfcfa;
  --screen-edge:#e7e0d2;
  --scan-box:#545a66;
  --green:#3aa757;
  --sky:#1f9bd7;
}
*{box-sizing:border-box;margin:0;padding:0}
html,body{width:798px;height:1200px;overflow:hidden;background:var(--page)}
body{position:relative;font-family:"Open Sans",sans-serif;color:var(--ink)}
.screen{position:absolute;width:152px;height:269px;overflow:hidden;
  background:radial-gradient(ellipse at 50% 45%,var(--screen-mid) 55%,var(--screen-edge) 100%)}
.screen--home{left:124px;top:84px;background:linear-gradient(160deg,#f1f1f1 0%,#e2e2e2 45%,#f3f3f3 70%,#ebe6dc 100%)}
.screen--about{left:320px;top:84px}
.screen--contact{left:514px;top:86px}
.screen--step1{left:122px;top:442px}
.screen--step2{left:320px;top:444px}
.screen--step3{left:516px;top:444px}
.screen--scan{left:124px;top:803px}
.appbar{height:22px;background:var(--bar);color:#fff;font:500 8px/22px "Montserrat",sans-serif;text-align:center;letter-spacing:.3px;position:relative}
.appbar svg{position:absolute;left:8px;top:6px}
.tabs{display:flex;height:22px;background:#eceae6;font:500 7px/22px "Montserrat",sans-serif}
.tab{flex:1;text-align:center;color:var(--ink)}
.tab.is-active{color:var(--orange);border-bottom:1.5px solid var(--orange);background:#f6f4f0}
.tagline{position:absolute;left:0;right:0;top:247px;text-align:center;font:500 9px "Montserrat",sans-serif;color:var(--ink)}
.home-icon{position:absolute;top:8px}
.brand{position:absolute;left:0;right:0;top:52px;text-align:center}
.brand-mark{display:inline-block;width:18px;height:18px;background:var(--orange)}
.brand-name{display:block;margin-top:6px;font:600 25px "Montserrat",sans-serif;color:var(--bar)}
.btn{position:absolute;left:21px;width:109px;height:28px;border-radius:14px;color:#fff;font:500 8.5px/28px "Montserrat",sans-serif;padding-left:39px;letter-spacing:.3px}
.btn svg{position:absolute;left:14px;top:6px}
.btn--scan{top:142px;background:var(--orange)}
.btn--howto{top:177px;background:var(--blue)}
.about-copy{padding:9px 11px 0;font-size:6.4px;line-height:10px;color:var(--ink)}
.about-copy p+p{margin-top:10px}
.contact-list{list-style:none;padding:20px 0 0 16px;font-size:6.4px;line-height:10px}
.contact-list li{position:relative;padding-left:15px;margin-bottom:6px}
.contact-list svg{position:absolute;left:0;top:1px}
.contact-list b{font-weight:600}
.step-badge{position:absolute;left:34px;top:61px}
.step-title{position:absolute;left:0;right:0;top:150px;text-align:center;font:700 8.5px "Montserrat",sans-serif;color:var(--orange)}
.step-copy{position:absolute;left:14px;right:14px;top:163px;text-align:center;font-size:6.4px;line-height:10px}
.pager{position:absolute;left:64px;top:250px;display:flex;gap:3px}
.pager i{width:4px;height:4px;border-radius:50%;background:#aaa}
.pager i:first-child{background:#444}
.next{position:absolute;left:132px;top:246px}
.scan-tools{position:absolute;left:0;top:33px;width:152px;height:14px}
.scan-frame{position:absolute;left:22px;top:75px}
</style>
</head>
<body>

<section class="screen screen--home">
  <svg class="home-icon" style="left:9px" width="12" height="12" viewBox="0 0 12 12"><circle cx="6" cy="6" r="5.5" fill="#fff" stroke="#bbb" stroke-width=".6"/><text x="6" y="8.6" font-size="7" font-style="italic" text-anchor="middle" fill="#555" font-family="serif">i</text></svg>
  <svg class="home-icon" style="left:131px" width="12" height="12" viewBox="0 0 12 12"><circle cx="6" cy="6" r="5.5" fill="#fff" stroke="#bbb" stroke-width=".6"/><path d="M8.4 5.2A2.6 2.6 0 1 0 8 7.6" fill="none" stroke="#666" stroke-width=".8"/><path d="M8.9 3.6v2h-2" fill="none" stroke="#666" stroke-width=".8"/></svg>
  <div class="brand"><span class="brand-mark"></span><span class="brand-name">Morevo</span></div>
  <div class="btn btn--scan"><svg width="16" height="16" viewBox="0 0 16 16" fill="none" stroke="#fff" stroke-width="1.5"><path d="M1 5V1h4M11 1h4v4M15 11v4h-4M5 15H1v-4M3 8h10"/></svg>START SCAN</div>
  <div class="btn btn--howto"><svg width="16" height="16" viewBox="0 0 16 16" fill="none" stroke="#fff" stroke-width="1.2"><circle cx="8" cy="8" r="7"/><path d="M6 6.2a2 2 0 1 1 2.6 1.9c-.5.2-.6.5-.6 1.1"/><circle cx="8" cy="11.6" r=".5" fill="#fff"/></svg>HOW TO</div>
  <p class="tagline">broden your reality</p>
</section>

<section class="screen screen--about">
  <header class="appbar"><svg width="11" height="9" viewBox="0 0 11 9" fill="none" stroke="#fff" stroke-width="1"><path d="M10 4.5H1M4.5 1 1 4.5 4.5 8"/></svg>ABOUT</header>
  <nav class="tabs"><span class="tab is-active">About</span><span class="tab">Contact</span></nav>
  <div class="about-copy">
    <p>Lorem Ipsum is simply dummy text of the printing and typesetting industry. Lorem Ipsum has been the industry's standard dummy text ever since the 1500s, when an unknown printer took a galley of type and scrambled it to make a type specimen book. It has survived not only five centuries, but also the leap into electronic typesetting, remaining essentially unchanged.</p>
    <p>It was popularised in the 1960s with the release of Typeron sheets containing Lorem Ipsum passages, and more recently with desktop publishing software like Quillby PageForge including versions of Lorem Ipsum.</p>
  </div>
  <p class="tagline">broden your reality</p>
</section>

<section class="screen screen--contact">
  <header class="appbar"><svg width="11" height="9" viewBox="0 0 11 9" fill="none" stroke="#fff" stroke-width="1"><path d="M10 4.5H1M4.5 1 1 4.5 4.5 8"/></svg>ABOUT</header>
  <nav class="tabs"><span class="tab">About</span><span class="tab is-active">Contact</span></nav>
  <ul class="contact-list">
    <li><svg width="9" height="12" viewBox="0 0 9 12"><path d="M4.5 0A4.5 4.5 0 0 0 0 4.5C0 8 4.5 12 4.5 12S9 8 9 4.5A4.5 4.5 0 0 0 4.5 0z" fill="var(--orange)"/><circle cx="4.5" cy="4.5" r="1.7" fill="#fff"/></svg>1010 Harbor Lane N.J 2051478<br>printing typesetting industry<br>Australia</li>
    <li><svg width="10" height="10" viewBox="0 0 10 10"><path d="M2 .5 4 3 3 4.3c.6 1.2 1.5 2.1 2.7 2.7L7 6l2.5 2-1 1.5C4.5 9.5.5 5.5.5 1.5z" fill="none" stroke="var(--orange)" stroke-width="1"/></svg><b>800 41270 33918<br>800 41270 33925</b></li>
    <li><svg width="10" height="8" viewBox="0 0 10 8"><rect width="10" height="8" fill="var(--orange)"/><path d="M0 0 5 4.5 10 0" fill="none" stroke="#fff" stroke-width=".8"/></svg><b>info@morevo.com<br>sales@morevo.com</b></li>
  </ul>
  <p class="tagline">broden your reality</p>
</section>

<section class="screen screen--step1">
  <header class="appbar"><svg width="11" height="9" viewBox="0 0 11 9" fill="none" stroke="#fff" stroke-width="1"><path d="M10 4.5H1M4.5 1 1 4.5 4.5 8"/></svg>HOW TO</header>
  <svg class="step-badge" width="84" height="84" viewBox="-42 -42 84 84"><circle r="41" fill="none" stroke="var(--orange)" stroke-width="1.3"/><polygon points="0,-27 6.3,-8.7 25.7,-8.3 10.2,3.3 15.9,21.8 0,10.8 -15.9,21.8 -10.2,3.3 -25.7,-8.3 -6.3,-8.7" fill="none" stroke="var(--orange)" stroke-width="3" stroke-linejoin="round" transform="translate(0,2)"/></svg>
  <p class="step-title">STEP 1</p>
  <p class="step-copy">Lorem Ipsum is simply dummy text of the printing and typesetting industry. Lorem Ipsum has been the industry's</p>
  <div class="pager"><i></i><i></i><i></i></div>
  <svg class="next" width="11" height="9" viewBox="0 0 11 9" fill="none" stroke="#444" stroke-width="1"><path d="M1 4.5h9M6.5 1 10 4.5 6.5 8"/></svg>
</section>

<section class="screen screen--step2">
  <header class="appbar"><svg width="11" height="9" viewBox="0 0 11 9" fill="none" stroke="#fff" stroke-width="1"><path d="M10 4.5H1M4.5 1 1 4.5 4.5 8"/></svg>HOW TO</header>
  <svg class="step-badge" width="84" height="84" viewBox="-42 -42 84 84"><defs><clipPath id="half-left"><rect x="-30" y="-30" width="30" height="60"/></clipPath></defs><circle r="41" fill="none" stroke="var(--orange)" stroke-width="1.3"/><g transform="translate(0,2)"><polygon points="0,-27 6.3,-8.7 25.7,-8.3 10.2,3.3 15.9,21.8 0,10.8 -15.9,21.8 -10.2,3.3 -25.7,-8.3 -6.3,-8.7" fill="var(--orange)" clip-path="url(#half-left)"/><polygon points="0,-27 6.3,-8.7 25.7,-8.3 10.2,3.3 15.9,21.8 0,10.8 -15.9,21.8 -10.2,3.3 -25.7,-8.3 -6.3,-8.7" fill="none" stroke="var(--orange)" stroke-width="3" stroke-linejoin="round"/></g></svg>
  <p class="step-title">STEP 2</p>
  <p class="step-copy">Lorem Ipsum is simply dummy text of the printing and typesetting industry. Lorem Ipsum has been the industry's</p>
  <div class="pager"><i></i><i></i><i></i></div>
  <svg class="next" width="11" height="9" viewBox="0 0 11 9" fill="none" stroke="#444" stroke-width="1"><path d="M1 4.5h9M6.5 1 10 4.5 6.5 8"/></svg>
</section>

<section class="screen screen--step3">
  <header class="appbar"><svg width="11" height="9" viewBox="0 0 11 9" fill="none" stroke="#fff" stroke-width="1"><path d="M10 4.5H1M4.5 1 1 4.5 4.5 8"/></svg>HOW TO</header>
  <svg class="step-badge" width="84" height="84" viewBox="-42 -42 84 84"><circle r="41" fill="none" stroke="var(--orange)" stroke-width="1.3"/><polygon points="0,-27 6.3,-8.7 25.7,-8.3 10.2,3.3 15.9,21.8 0,10.8 -15.9,21.8 -10.2,3.3 -25.7,-8.3 -6.3,-8.7" fill="var(--orange)" stroke="var(--orange)" stroke-width="3" stroke-linejoin="round" transform="translate(0,2)"/></svg>
  <p class="step-title">STEP 3</p>
  <p class="step-copy">Lorem Ipsum is simply dummy text of the printing and typesetting industry. Lorem Ipsum has been the industry's</p>
  <div class="pager"><i></i><i></i><i></i></div>
  <svg class="next" width="11" height="9" viewBox="0 0 11 9" fill="none" stroke="#444" stroke-width="1"><path d="M1 4.5h9M6.5 1 10 4.5 6.5 8"/></svg>
</section>

<section class="screen screen--scan">
  <header class="appbar"><svg width="11" height="9" viewBox="0 0 11 9" fill="none" stroke="#fff" stroke-width="1"><path d="M10 4.5H1M4.5 1 1 4.5 4.5 8"/></svg>SCAN</header>
  <svg class="scan-tools" viewBox="0 0 152 14">
    <circle cx="44" cy="7" r="6.5" fill="var(--orange)"/><path d="M41.5 5.8 44 8.3 46.5 5.8" fill="none" stroke="#fff" stroke-width="1.1"/>
    <circle cx="78" cy="7" r="6.5" fill="var(--green)"/><path d="M79 3 75.8 7.6h2.4L77 11l3.2-4.6h-2.4z" fill="#fff"/>
    <circle cx="112" cy="7" r="6.5" fill="var(--sky)"/><text x="112" y="10" font-size="8" font-weight="700" text-anchor="middle" fill="#fff" font-family="Montserrat,sans-serif">?</text>
  </svg>
  <svg class="scan-frame" width="110" height="146" viewBox="0 0 110 146" fill="none" stroke="var(--scan-box)" stroke-width="6">
    <path d="M3 20V3h20M87 3h20v17M107 126v17H87M23 143H3v-17"/>
    <rect x="12" y="14" width="85" height="122" fill="var(--scan-box)" stroke="none"/>
  </svg>
</section>

</body>
</html>
```